Re-style home page - eye-catching and unique design for social commerce website

We need a new concept design for Trondix's home page.
We don't want to make huge changes but creating a more professional and eye-catching style.

We need to look very serious like a professional services company and in the same time to look like a social network for e-commerce.

Our logo is very captive and you can use to creating something of harmonious.

This is a re-style and I'm excepted to see unique and fresh design like Glimmora.
Updates

Target Market(s)

e-commerce and social

Industry/Entity Type

Social

Number of Pages Required

1 page

Font styles to use
Serif
Sans Serif

Requirements
Must have
• An eye-catching result.
• Search bar with logo and Login How it works and business
• The slogan with login and signup.
• Footer links.
Nice to have
• I would like to open the home page and see only two clear ways:
• -Consumer
• --Search
• --The slogan
• --Login and Signup
• --How it works
• -Business
• --Go to Business area
• Background: City, Shopping.
Should not have
• Scrollbar style!

```html
<!DOCTYPE html>
<html lang="en">
<head>
<meta charset="utf-8">
<title>Trondix — Shop Directly From Your Profile</title>
<link rel="stylesheet" href="https://fonts.googleapis.com/css2?family=Arimo:wght@400;700&family=Lato:wght@400;700;900&display=swap">
<style>
  :root {
    --header-bg: #2b2b2b;
    --page-bg: #3c3c3c;
    --card-head: rgba(40, 40, 40, 0.82);
    --card-body: #2d2d2d;
    --white: #ffffff;
    --muted: #d0d0d0;
    --accent: #f7c21a;
    --accent-deep: #f2a900;
    --social: #4a66a6;
    --social-dark: #3d5794;
    --field-border: #cfcfcf;
    --rainbow: linear-gradient(90deg, #2d4fc8 0%, #8a3fb8 30%, #e0455a 60%, #f0a85a 80%, #f6d64a 100%);
  }
  * { box-sizing: border-box; margin: 0; padding: 0; }
  html, body { width: 1200px; height: 979px; overflow: hidden; }
  body { position: relative; font-family: "Lato", Arial, sans-serif; background: var(--white); color: var(--white); }

  .hero-photo {
    position: absolute; left: 0; top: 80px; width: 1200px; height: 850px;
    background:
      radial-gradient(ellipse 260px 300px at 1040px 380px, rgba(88, 104, 52, 0.75), transparent 70%),
      radial-gradient(ellipse 420px 260px at 180px 260px, rgba(170, 170, 170, 0.55), transparent 70%),
      radial-gradient(ellipse 160px 200px at 210px 420px, rgba(150, 95, 80, 0.55), transparent 70%),
      linear-gradient(180deg, #4a4a4a 0%, #3d3d3d 60%, #353535 100%);
  }
  .hero-photo::after { content: ""; position: absolute; inset: 0; background: rgba(30, 30, 30, 0.25); }

  .site-header { position: absolute; left: 0; top: 0; width: 1200px; height: 80px; background: var(--header-bg); }
  .site-header::before { content: ""; position: absolute; left: 0; top: 0; width: 100%; height: 3px; background: var(--rainbow); }
  .brand { position: absolute; left: 156px; top: 30px; display: flex; align-items: center; gap: 10px; font-family: "Lato", Arial, sans-serif; font-weight: 700; font-size: 19px; color: var(--white); }
  .brand-mark { width: 16px; height: 16px; border-radius: 50%; background: var(--accent); }

  .search { position: absolute; left: 327px; top: 23px; width: 402px; height: 35px; display: flex; border: 2px solid #111; background: #111; }
  .search-input { flex: 1; background: var(--white); font-family: "Lato", Arial, sans-serif; font-style: italic; font-size: 12px; color: #999; padding: 10px 18px; border-right: 1px solid #111; }
  .search-button { width: 67px; background: var(--accent); color: #3a2a00; font-weight: 700; font-size: 13px; display: flex; align-items: center; justify-content: center; }

  .main-nav { position: absolute; top: 34px; font-family: "Arimo", Arial, sans-serif; font-weight: 700; font-size: 13px; }
  .main-nav a { position: absolute; color: var(--white); text-decoration: none; white-space: nowrap; }

  .signup-card { position: absolute; left: 326px; top: 131px; width: 584px; height: 718px; border: 1px solid #222; }
  .signup-card::before { content: ""; position: absolute; left: -1px; top: -1px; width: 586px; height: 4px; background: var(--rainbow); z-index: 2; }
  .card-head { position: absolute; left: 0; top: 0; width: 100%; height: 102px; background: var(--card-head); }
  .card-title { position: absolute; left: 26px; top: 25px; font-family: "Arimo", Arial, sans-serif; font-size: 26px; font-weight: 400; letter-spacing: 0.1px; }
  .card-subtitle { position: absolute; left: 27px; top: 61px; font-family: "Arimo", Arial, sans-serif; font-size: 16px; color: var(--muted); }

  .feed-topics { position: absolute; left: 0; top: 102px; width: 100%; height: 284px;
    background: linear-gradient(150deg, #5c5c5c 0%, #6d6d6d 40%, #505050 75%, #444 100%); }
  .topic { position: absolute; display: flex; align-items: center; gap: 8px; font-family: "Arimo", Arial, sans-serif; font-weight: 700; font-size: 14.5px; color: var(--white); white-space: nowrap; }
  .topic svg { width: 20px; height: 20px; fill: var(--accent); }

  .card-body { position: absolute; left: 0; top: 386px; width: 100%; height: 332px; background: var(--card-body); }
  .slogan { position: absolute; left: 0; top: 18px; width: 100%; padding-left: 8px; text-align: center; font-size: 17px; font-weight: 700; }
  .social-button { position: absolute; left: 188px; top: 50px; width: 219px; height: 36px; background: var(--social); display: flex; align-items: center; }
  .social-button .mark { width: 37px; height: 100%; background: var(--social-dark); }
  .social-button span { flex: 1; text-align: center; font-size: 11px; font-weight: 900; letter-spacing: 0.8px; }
  .divider { position: absolute; left: 202px; top: 102px; width: 190px; display: flex; align-items: center; gap: 12px; font-size: 13px; color: #ddd; }
  .divider::before, .divider::after { content: ""; flex: 1; height: 1px; background: #4a4a4a; }
  .field { position: absolute; left: 188px; width: 219px; height: 33px; background: var(--white); border: 1px solid var(--field-border); box-shadow: inset 0 2px 3px rgba(0,0,0,0.15); font-size: 12px; color: #888; padding: 9px 13px; }
  .field-email { top: 137px; }
  .field-password { top: 187px; }
  .submit { position: absolute; left: 188px; top: 237px; width: 219px; height: 36px; background: linear-gradient(180deg, #ffd21f, var(--accent-deep)); color: #2a2000; font-size: 14px; display: flex; align-items: center; justify-content: center; }
  .legal { position: absolute; left: 175px; top: 290px; width: 245px; text-align: center; font-size: 9px; line-height: 14px; color: #eee; }

  .scroll-tab { position: absolute; left: 580px; top: 904px; width: 43px; height: 27px; background: var(--white); display: flex; align-items: center; justify-content: center; }
  .footer-strip { position: absolute; left: 0; top: 930px; width: 1200px; height: 49px; background: var(--white); }
</style>
</head>
<body>
  <div class="hero-photo" role="img" aria-label="Blurred photo of hands typing on a laptop beside a green plant"></div>

  <header class="site-header">
    <div class="brand">Trondix <span class="brand-mark"></span></div>
    <div class="search">
      <div class="search-input">Type your search here...</div>
      <div class="search-button">search</div>
    </div>
    <nav class="main-nav">
      <a href="#" style="left:885px">Login</a>
      <a href="#" style="left:962px">How it Works</a>
      <a href="#" style="left:1087px">Business</a>
    </nav>
  </header>

  <section class="signup-card">
    <div class="card-head">
      <h1 class="card-title">Shop Directly From&nbsp; Your Profile</h1>
      <p class="card-subtitle">Set up your Feed</p>
    </div>

    <div class="feed-topics" role="img" aria-label="Photo of a laptop keyboard behind the feed topics">
      <svg width="0" height="0" style="position:absolute">
        <defs>
          <symbol id="i-run" viewBox="0 0 20 20"><circle cx="12" cy="3" r="2.2"/><path d="M9 6h4l2 4 3 1-.6 1.6-4-1.4-1-1.6-1.2 3 3 2.4-1.2 4.6-1.8-.4.8-3.6-3.4-2.2-1.4 3L3 15l.6-1.6 3 .4L9.5 8 7 9 5.6 11 4.2 10 6.4 7z"/></symbol>
          <symbol id="i-food" viewBox="0 0 20 20"><circle cx="11" cy="10" r="6"/><rect x="2" y="3" width="1.6" height="14"/><rect x="17" y="3" width="1.6" height="14"/></symbol>
          <symbol id="i-paw" viewBox="0 0 20 20"><ellipse cx="10" cy="13" rx="4.5" ry="3.8"/><circle cx="4" cy="8" r="2"/><circle cx="8" cy="4.5" r="2"/><circle cx="12.5" cy="4.5" r="2"/><circle cx="16.2" cy="8" r="2"/></symbol>
          <symbol id="i-spa" viewBox="0 0 20 20"><circle cx="9" cy="4" r="2.4"/><path d="M3 16h15v2H3zM5 15l3-7h3l4 4h3v3z"/></symbol>
          <symbol id="i-cap" viewBox="0 0 20 20"><path d="M10 3 1 8l9 5 9-5z"/><path d="M5 11v4c2 2 8 2 10 0v-4l-5 3z"/></symbol>
          <symbol id="i-tools" viewBox="0 0 20 20"><path d="M3 15 13 5l2 2L5 17z"/><path d="M5 3l12 12-2 2L3 5z"/></symbol>
          <symbol id="i-car" viewBox="0 0 20 20"><path d="M4 5h12l2 5v6h-3v-2H5v2H2v-6z"/><rect x="5" y="6.5" width="10" height="3" fill="#555"/></symbol>
          <symbol id="i-mask" viewBox="0 0 20 20"><path d="M2 4c3 1 6 1 9 0 0 6-2 10-4.5 10S2 10 2 4z"/><path d="M10 8c3 1 5 1 8 0 0 6-2 9-4 9s-4-3-4-9z"/></symbol>
          <symbol id="i-hotel" viewBox="0 0 20 20"><path d="M4 2h12v16h-4v-4H8v4H4z"/></symbol>
        </defs>
      </svg>

      <div class="topic" style="left:26px;top:29px"><svg><use href="#i-run"/></svg>Active Life</div>
      <div class="topic" style="left:189px;top:29px"><svg><use href="#i-spa"/></svg>&nbsp;Beauty &amp; Spas</div>
      <div class="topic" style="left:372px;top:30px"><svg><use href="#i-car"/></svg>&nbsp;Automotive</div>

      <div class="topic" style="left:26px;top:79px"><svg><use href="#i-food"/></svg>Food</div>
      <div class="topic" style="left:189px;top:79px"><svg><use href="#i-cap"/></svg>&nbsp;Education</div>
      <div class="topic" style="left:372px;top:80px"><svg><use href="#i-mask"/></svg>&nbsp;Arts &amp; Entertainment</div>

      <div class="topic" style="left:26px;top:130px"><svg><use href="#i-paw"/></svg>Pets</div>
      <div class="topic" style="left:189px;top:130px"><svg><use href="#i-tools"/></svg>&nbsp;Local Services</div>
      <div class="topic" style="left:372px;top:131px"><svg><use href="#i-hotel"/></svg>&nbsp;Hotels</div>

      <div class="topic" style="left:26px;top:181px"><svg><use href="#i-run"/></svg>Active Life</div>
      <div class="topic" style="left:189px;top:181px"><svg><use href="#i-spa"/></svg>&nbsp;Beauty &amp; Spas</div>
      <div class="topic" style="left:372px;top:182px"><svg><use href="#i-car"/></svg>&nbsp;Automotive</div>

      <div class="topic" style="left:26px;top:229px"><svg><use href="#i-food"/></svg>Food</div>
      <div class="topic" style="left:189px;top:229px"><svg><use href="#i-cap"/></svg>&nbsp;Education</div>
      <div class="topic" style="left:372px;top:230px"><svg><use href="#i-mask"/></svg>&nbsp;Shopping</div>
    </div>

    <div class="card-body">
      <p class="slogan">Save your time. Live Better.</p>
      <div class="social-button"><div class="mark"></div><span>SIGN IN WITH FRIENDLOOP</span></div>
      <div class="divider">or</div>
      <div class="field field-email">Email</div>
      <div class="field field-password">Password</div>
      <div class="submit">Sign Up</div>
      <p class="legal">Creating an account you agree with Terms of Service and Privacy Policy</p>
    </div>
  </section>

  <div class="scroll-tab">
    <svg width="16" height="12" viewBox="0 0 16 12"><path d="M1 2l7 7 7-7" fill="none" stroke="#333" stroke-width="3.5"/></svg>
  </div>
  <div class="footer-strip"></div>
</body>
</html>
```